Harbormoor Property Institute Needs Banner Designs

I just launched an online real estate school at www.harbormoorpropertyinstitute.com

I am seeking designers to work on 2 banners (listed seperately) as well as a a Facebook design. This listing is for 1 of 2 banners.

First banner I intend to use on different job offering web sites. So "Launch your career into Real Estate" could be the concept. i'm open to 1 sentence pitch's. please look at my website to view graphics and colors.

```html
<!DOCTYPE html>
<html lang="en">
<head>
<meta charset="utf-8">
<title>Harbormoor Property Institute – Launch Your Career Into Real Estate</title>
<link rel="stylesheet" href="https://fonts.googleapis.com/css2?family=Open+Sans:wght@600;700;800&display=swap">
<style>
  :root {
    --navy: #0d3d7a;
    --navy-edge: #0a2f5f;
    --orange: #f7a21b;
    --orange-light: #ffc640;
    --orange-dark: #e58a0c;
    --white: #ffffff;
    --ink: #2b2418;
    --scene-light: #f6ecd8;
    --scene-mid: #d9c7a4;
    --scene-dark: #8d7a5c;
  }
  * { margin: 0; padding: 0; box-sizing: border-box; }
  html, body { width: 1200px; height: 149px; overflow: hidden; background: var(--white); }
  .banner {
    position: relative;
    width: 1200px;
    height: 149px;
    overflow: hidden;
    font-family: "Open Sans", Arial, sans-serif;
  }
  .scene {
    position: absolute;
    inset: 0;
    background:
      radial-gradient(ellipse 260px 160px at 560px 40px, rgba(255,255,255,0.85), transparent 70%),
      linear-gradient(90deg, var(--scene-dark) 0%, var(--scene-mid) 28%, var(--scene-light) 50%, var(--scene-mid) 75%, #b8a27c 100%);
  }
  .pitch-panel {
    position: absolute;
    left: 0; top: 0;
    width: 358px;
    height: 149px;
    background: var(--navy);
    border-right: 3px solid var(--navy-edge);
    display: flex;
    flex-direction: column;
    align-items: center;
    justify-content: center;
    text-transform: uppercase;
    color: var(--white);
    text-align: center;
    line-height: 1;
  }
  .pitch-lead, .pitch-tail { font-size: 21px; font-weight: 700; letter-spacing: 0.3px; }
  .pitch-key {
    font-size: 52px;
    font-weight: 800;
    color: var(--orange);
    margin: 3px 0 4px;
  }
  .tagline {
    position: absolute;
    left: 399px;
    top: 83px;
    font-size: 22px;
    font-weight: 600;
    color: var(--ink);
  }
  .brand {
    position: absolute;
    left: 712px;
    top: 62px;
    width: 128px;
    text-align: center;
    font-size: 15px;
    font-weight: 600;
    line-height: 1.15;
    color: var(--ink);
  }
  .cta {
    position: absolute;
    left: 936px;
    top: 40px;
    width: 226px;
    text-align: center;
  }
  .cta-note {
    font-size: 17px;
    font-weight: 700;
    color: var(--ink);
    margin-bottom: 6px;
  }
  .cta-button {
    display: block;
    height: 46px;
    line-height: 46px;
    border-radius: 23px;
    background: linear-gradient(180deg, var(--orange-light) 0%, var(--orange) 55%, var(--orange-dark) 100%);
    color: var(--ink);
    font-size: 24px;
    font-weight: 700;
    text-decoration: none;
  }
</style>
</head>
<body>
  <div class="banner">
    <div class="scene" role="img" aria-label="Businessman in a suit looking out over a sunlit city skyline"></div>

    <div class="pitch-panel">
      <span class="pitch-lead">Launch your</span>
      <span class="pitch-key">Career</span>
      <span class="pitch-tail">Into real estate</span>
    </div>

    <p class="tagline">Quick, Easy, and Affordable</p>

    <p class="brand">Harbormoor Property Institute</p>

    <div class="cta">
      <p class="cta-note">For More Details</p>
      <a class="cta-button" href="https://www.harbormoorpropertyinstitute.com">Visit Now</a>
    </div>
  </div>
</body>
</html>
```